Creation of website design for digital SAAS service for congresses, lectures and training

We are a startup in southern Germany that wants to prepare the digital bridge for all events so that the listener of a lecture or congress can digitally save the presentations and their notes. As a result, he is involved in the lecture much more intensively and will benefit from it. He can then use the app to ask the speaker / organizer to call you back using one of the picked slides. These are the leads that are generated from the events. It is a subscription model for the organizer or speakers so that he generates better results and more leads from his event. The application is running productively and can be used as a demo with a mobile phone at https://dorvane.net/demosession.html. Simply scan the QR code and pick the slides you like.
The website is a bit gruesome ..... that's why I need YOU!

The logo is Lumbo - our maksottchen, because he picks and saves the exciting slides from the presentation .....

The designer can get a free trial account for a month to get to know the app. Ends automatically!
https://app.dorvane.net/subscription/plans

Target Market(s)

Trade fair organizers, congress organizers, product management, hotel chains, associations, schools, universities, marketing organizations

Font styles to use
Sans Serif

Requirements
Must have
• The customer group are, on the one hand, marketing and sales professionals who should book the service for their customers and prospects so that more leads come from the events.
The login for the service can be done on any internet-enabled device with a browser.
Legal requirements regarding options for cookies and terms and conditions
Multilingualism DE and EN would then have to be considered technically.
The whole thing should then run on a wordpress version 5.41.
If images / photos are used, the copyright question must be clarified - what costs arise from the use and how is this to be documented if necessary.
Nice to have
• Maybe someone also creates an animation that explains the picking process nicely ... and maps the two user groups. Everyone should find themselves
Should not have
• Bad design and layout - I can top that myself!

```html
<!DOCTYPE html>
<html lang="en">
<head>
<meta charset="utf-8">
<title>dorvane – homepage variants</title>
<link rel="stylesheet" href="https://fonts.googleapis.com/css2?family=Poppins:wght@500;600;700&family=Roboto:wght@400;500;700&display=swap">
<style>
:root{
  --stage:#dcdcdc;
  --green:#1f7f3f;
  --green-soft:#5aa874;
  --green-pale:#a9d1b5;
  --red:#e8141b;
  --blue-btn:#35a8e0;
  --ink:#2a2a2a;
  --muted:#6a6a6a;
  --band:#a9b8d3;
  --footer:#2b2b2e;
  --white:#ffffff;
}
*{box-sizing:border-box;margin:0;padding:0}
html,body{width:1200px;height:692px;overflow:hidden}
body{background:var(--stage);font-family:"Roboto",Arial,sans-serif;color:var(--ink);position:relative}
.page{position:absolute;top:48px;width:685px;height:1254px;background:var(--white);transform:scale(.4754);transform-origin:0 0;overflow:hidden;box-shadow:0 2px 6px rgba(0,0,0,.12)}
.page--a{left:70px}.page--b{left:437px}.page--c{left:804px}

/* header */
.site-header{position:absolute;top:0;left:0;right:0;height:60px;z-index:5}
.brand{position:absolute;left:62px;top:22px;display:flex;align-items:center;gap:6px;font-family:"Poppins",sans-serif;font-weight:600;font-size:20px;color:#3a3a3a}
.brand-dot{width:14px;height:14px;border-radius:50%;background:var(--green)}
.nav{position:absolute;left:172px;top:25px;display:flex;gap:10px;font-size:8.5px;font-weight:500;color:#222}
.nav .is-active{color:var(--red)}
.btn{display:inline-flex;align-items:center;justify-content:center;border-radius:14px;color:var(--white);font-weight:700;font-size:8.5px;white-space:nowrap}
.btn-green{background:var(--green)}
.btn-blue{background:var(--blue-btn)}
.nav-cta{position:absolute;left:526px;top:17px;width:95px;height:26px}

/* hero */
.hero{position:absolute;top:0;left:0;width:685px;height:391px;background:#f2f2f2;overflow:hidden}
.hero-texture{position:absolute;left:0;right:0;bottom:0;height:200px;background:linear-gradient(180deg,rgba(242,242,242,0) 0%,rgba(236,205,210,.55) 60%,rgba(240,228,230,.6) 100%)}
.hero-copy{position:absolute;left:62px;top:102px;z-index:3}
.hero-title{font-family:"Poppins",sans-serif;font-weight:600;font-size:18px;line-height:24px;width:300px}
.hero-lead{margin-top:12px;font-size:9px;line-height:16px;width:310px}
.quick{position:absolute;top:222px;z-index:3}
.quick--pickers{left:62px}
.quick--speaker{left:276px}
.quick-divider{position:absolute;left:262px;top:222px;width:1px;height:90px;background:#d8d8d8;z-index:3}
.quick h3{font-family:"Poppins",sans-serif;font-weight:600;font-size:9.5px}
.quick p{margin-top:6px;font-size:8.5px;line-height:13px;color:var(--muted);width:150px}
.code-label{margin-top:10px;font-size:8.5px;font-weight:500;color:var(--green)}
.code-row{position:absolute;top:63px;left:0;display:flex;align-items:center;width:200px}
.code-input{width:100px;height:25px;border-radius:13px;background:var(--white);box-shadow:0 1px 3px rgba(0,0,0,.12);font-size:7px;color:#555;display:flex;align-items:center;padding-left:10px}
.code-row .btn{width:98px;height:25px;margin-left:-6px}
.speaker-row{position:absolute;top:63px;left:1px;display:flex;align-items:center}
.speaker-row .btn-blue{width:72px;height:25px}
.speaker-row .or{font-size:8px;color:#444;width:24px;text-align:center}
.speaker-row .btn-green{width:75px;height:25px}

/* illustration placeholders */
.art{position:absolute;border-radius:6px;background:linear-gradient(135deg,var(--green-pale) 0%,var(--green-soft) 100%);z-index:1}
.phone{position:absolute;border:5px solid #111;border-radius:16px;background:#111;z-index:2}
.phone-screen{width:100%;height:100%;border-radius:11px;background:linear-gradient(180deg,#ffffff 0%,#f4f4f4 55%,#e2e2e2 100%)}
.phone-screen--demo{background:linear-gradient(180deg,#ffffff 0%,#ffffff 30%,#d9412f 31%,#c53423 48%,#ffffff 49%,#f2f2f2 100%)}

/* speakers band */
.speakers{position:absolute;top:391px;left:0;width:685px;height:392px;background:radial-gradient(ellipse at 20% 80%,#9fb4d6 0%,var(--band) 55%,#aab6cf 100%)}
.speakers-title{position:absolute;top:33px;left:0;right:0;text-align:center;font-family:"Poppins",sans-serif;font-weight:600;font-size:18px;line-height:24px;color:var(--white)}
.card{position:absolute;top:104px;width:176px;height:233px;background:var(--white);border-radius:8px;text-align:center;padding:0 10px}
.card:nth-of-type(1){left:63px}.card:nth-of-type(2){left:254px}.card:nth-of-type(3){left:446px}
.card-icon{width:40px;height:40px;border-radius:50%;margin:19px auto 0}
.card-icon--dark{background:#2f2f33}
.card-icon--green{background:var(--green)}
.card h3{margin-top:14px;font-size:9.5px;font-weight:500;color:#222}
.card .card-sub{margin-top:3px;font-size:7.5px;color:#555}
.card .card-body{margin-top:9px;font-size:8.3px;line-height:15.7px;color:#555}
.learn{position:absolute;left:0;right:0;bottom:15px;font-size:8.5px;font-weight:700;color:var(--green);display:flex;justify-content:center;align-items:center;gap:4px}
.learn svg{width:8px;height:8px}

/* demo */
.demo{position:absolute;top:783px;left:0;width:685px;height:318px;background:var(--white);overflow:hidden}
.demo-copy{position:absolute;left:280px;top:78px;width:340px;z-index:3}
.demo-title{font-family:"Poppins",sans-serif;font-weight:600;font-size:18px}
.demo-text{margin-top:12px;font-size:8.6px;line-height:16px;color:#555}
.demo-note{margin-top:12px;font-size:8.6px;font-weight:500;color:#222}
.demo .btn{margin-top:19px;width:95px;height:25px}

/* footer */
.site-footer{position:absolute;top:1101px;left:0;width:685px;height:153px;background:var(--footer);color:var(--white)}
.contact{position:absolute;top:35px;display:flex;align-items:center;gap:7px}
.contact:nth-of-type(1){left:144px}.contact:nth-of-type(2){left:292px}.contact:nth-of-type(3){left:431px}
.contact-icon{width:30px;height:30px;border-radius:50%;background:var(--green);display:flex;align-items:center;justify-content:center}
.contact-icon svg{width:13px;height:13px}
.contact p{font-size:8.5px;line-height:14px;font-weight:500}
.footer-rule{position:absolute;top:79px;left:62px;width:560px;height:1px;background:#4a4a4e}
.footer-links{position:absolute;top:101px;left:62px;display:flex;gap:8px;font-size:8px}
.footer-links span.sep{color:#aaa}
.copyright{position:absolute;top:124px;left:62px;font-size:8px}
.socials{position:absolute;top:108px;left:493px;display:flex;gap:5px}
.socials span{width:28px;height:28px;border-radius:50%;border:1.5px solid var(--red)}
</style>
</head>
<body>

<svg width="0" height="0" style="position:absolute" aria-hidden="true">
  <defs>
    <symbol id="i-phone" viewBox="0 0 24 24"><path fill="#fff" d="M6.6 10.8a15.1 15.1 0 0 0 6.6 6.6l2.2-2.2c.3-.3.7-.4 1-.2 1.1.4 2.3.6 3.6.6.6 0 1 .4 1 1V20c0 .6-.4 1-1 1A17 17 0 0 1 3 4c0-.6.4-1 1-1h3.5c.6 0 1 .4 1 1 0 1.3.2 2.5.6 3.6.1.3 0 .7-.2 1z"/></symbol>
    <symbol id="i-landline" viewBox="0 0 24 24"><path fill="#fff" d="M3 9c5-4 13-4 18 0l-2 3-3-1V9H8v2l-3 1zM6 13h12l2 7H4zm6 1.5a2.5 2.5 0 1 0 0 5 2.5 2.5 0 0 0 0-5z"/></symbol>
    <symbol id="i-mail" viewBox="0 0 24 24"><path fill="#fff" d="M3 5h18v14H3zm2 2v.5l7 5 7-5V7zm0 3v7h14v-7l-7 5z"/></symbol>
    <symbol id="i-arrow" viewBox="0 0 24 24"><circle cx="12" cy="12" r="11" fill="#1f7f3f"/><path fill="#fff" d="M10 7l5 5-5 5-1.4-1.4L12.2 12 8.6 8.4z"/></symbol>
  </defs>
</svg>

<!-- Variant A -->
<section class="page page--a">
  <header class="site-header">
    <div class="brand"><span>dorvane</span><span class="brand-dot"></span></div>
    <nav class="nav"><span class="is-active">Home</span><span>Subscription variants</span><span>Participant / picker</span><span>speaker</span><span>organizer</span><span>En ⌄</span></nav>
    <span class="btn btn-green nav-cta">Risk-free testing</span>
  </header>
  <div class="hero">
    <div class="hero-texture" role="img" aria-label="Soft pink abstract wave texture"></div>
    <div class="art" role="img" aria-label="Mascot illustration reaching for the app" style="left:430px;top:82px;width:250px;height:258px"></div>
    <div class="phone" style="left:478px;top:80px;width:118px;height:242px"><div class="phone-screen" role="img" aria-label="Mobile app screen showing the presentation code entry"></div></div>
    <div class="hero-copy">
      <h1 class="hero-title">For the pickers:just pick your important slides</h1>
      <p class="hero-lead">Do you want qualified results of your marketing events for the further processing of the leads?</p>
    </div>
    <div class="quick quick--pickers">
      <h3>Quickstart for pickers:</h3>
      <p>Attend the lecture and pick your slides</p>
      <div class="code-label">Presentation code</div>
      <div class="code-row"><span class="code-input">presentation code</span><span class="btn btn-green">Join the presentation</span></div>
    </div>
    <div class="quick-divider"></div>
    <div class="quick quick--speaker">
      <h3>Speaker Login:</h3>
      <p>Register for your lectureshare or register.</p>
      <div class="speaker-row"><span class="btn btn-blue">Register</span><span class="or">or</span><span class="btn btn-green">To Register</span></div>
    </div>
  </div>
  <div class="speakers" role="img" aria-label="Blue backdrop with faint network pattern"></div>
  <div class="speakers" style="background:none">
    <h2 class="speakers-title">For the speakers: find your leads, get<br>feedback from the event</h2>
    <article class="card"><div class="card-icon card-icon--dark"></div><h3>Speaker, presenter with online PC</h3><p class="card-sub">The laptop must be online!</p><p class="card-body">Simply start the presentation in Slidemaker or other applications. Then call the dorvane app in the browser on app.dorvane.net. After logging in and starting the transmission, the lecture can proceed as normal.</p><div class="learn">LEARN MORE <svg><use href="#i-arrow"/></svg></div></article>
    <article class="card"><div class="card-icon card-icon--green"></div><h3>Listener = picker</h3><p class="card-sub">Conference participants, training guests,</p><p class="card-body">The audience starts the session by scanning the QR code or entering the dorvane code on https://dorvane.net. As soon as an interesting slide is shown, it can be picked using a button.<br>The picked slides can also be saved</p><div class="learn">LEARN MORE <svg><use href="#i-arrow"/></svg></div></article>
    <article class="card"><div class="card-icon card-icon--dark"></div><h3>Conference organizer event agency</h3><p class="card-sub">Planning and provision of the session ID</p><p class="card-body">We offer the pre-planning of a congress with many seasons about the lecture title, name of the speaker, room, time etc. We provide evaluations of the number of logged in pickers and their contact requests in various forms.</p><div class="learn">LEARN MORE <svg><use href="#i-arrow"/></svg></div></article>
  </div>
  <div class="demo">
    <div class="art" role="img" aria-label="Mascot illustration holding the app" style="left:55px;top:52px;width:175px;height:210px"></div>
    <div class="phone" style="left:125px;top:62px;width:90px;height:190px"><div class="phone-screen phone-screen--demo" role="img" aria-label="Mobile app screen of an example session"></div></div>
    <div class="demo-copy">
      <h2 class="demo-title">Talk to us for a demo!</h2>
      <p class="demo-text">We are currently still in the development process of the app! The basic functions are already finished and can be demonstrated.But we wanted to provide a sophisticated tool for you and your customers and we need test feedback. If you are interested, just get in touch and we will arrange a free test.</p>
      <p class="demo-note">No productive operation yet, ie no data is saved on the server.</p>
      <span class="btn btn-green">GET DEMO</span>
    </div>
  </div>
  <footer class="site-footer">
    <div class="contact"><span class="contact-icon"><svg><use href="#i-phone"/></svg></span><p>Telephone:<br>49-15120438816</p></div>
    <div class="contact"><span class="contact-icon"><svg><use href="#i-landline"/></svg></span><p>Landline:<br>+49711230574</p></div>
    <div class="contact"><span class="contact-icon"><svg><use href="#i-mail"/></svg></span><p>E-mail:<br>contact@dorvane.net</p></div>
    <div class="footer-rule"></div>
    <div class="footer-links"><span>Home</span><span class="sep">|</span><span>imprint</span><span class="sep">|</span><span>privacy</span><span class="sep">|</span><span>Contact</span><span class="sep">|</span><span>Terms &amp; Conditions</span><span class="sep">|</span><span>Privacy Statement</span></div>
    <p class="copyright">dorvane © 2020 All rights reserved.</p>
    <div class="socials"><span></span><span></span><span></span><span></span></div>
  </footer>
</section>

<!-- Variant B -->
<section class="page page--b">
  <header class="site-header">
    <div class="brand"><span>dorvane</span><span class="brand-dot"></span></div>
    <nav class="nav"><span class="is-active">Home</span><span>Subscription variants</span><span>Participant / picker</span><span>speaker</span><span>organizer</span><span>En ⌄</span></nav>
    <span class="btn btn-green nav-cta">Risk-free testing</span>
  </header>
  <div class="hero">
    <div class="hero-texture" role="img" aria-label="Soft pink abstract wave texture"></div>
    <div class="art" role="img" aria-label="Small mascot illustration at the edge" style="left:0;top:150px;width:44px;height:130px;border-radius:0 6px 6px 0"></div>
    <div class="art" role="img" aria-label="Mascot illustration beside the app" style="left:432px;top:160px;width:72px;height:125px"></div>
    <div class="phone" style="left:512px;top:80px;width:118px;height:242px"><div class="phone-screen" role="img" aria-label="Mobile app screen showing the presentation code entry"></div></div>
    <div class="hero-copy">
      <h1 class="hero-title">For the pickers:just pick your important slides</h1>
      <p class="hero-lead">Do you want qualified results of your marketing events for the further processing of the leads?</p>
    </div>
    <div class="quick quick--pickers">
      <h3>Quickstart for pickers:</h3>
      <p>Attend the lecture and pick your slides</p>
      <div class="code-label">Presentation code</div>
      <div class="code-row"><span class="code-input">presentation code</span><span class="btn btn-green">Join the presentation</span></div>
    </div>
    <div class="quick-divider"></div>
    <div class="quick quick--speaker">
      <h3>Speaker Login:</h3>
      <p>Register for your lectureshare or register.</p>
      <div class="speaker-row"><span class="btn btn-blue">Register</span><span class="or">or</span><span class="btn btn-green">To Register</span></div>
    </div>
  </div>
  <div class="speakers" role="img" aria-label="Blue backdrop with faint network pattern"></div>
  <div class="speakers" style="background:none">
    <h2 class="speakers-title">For the speakers: find your leads, get<br>feedback from the event</h2>
    <article class="card"><div class="card-icon card-icon--dark"></div><h3>Speaker, presenter with online PC</h3><p class="card-sub">The laptop must be online!</p><p class="card-body">Simply start the presentation in Slidemaker or other applications. Then call the dorvane app in the browser on app.dorvane.net. After logging in and starting the transmission, the lecture can proceed as normal.</p><div class="learn">LEARN MORE <svg><use href="#i-arrow"/></svg></div></article>
    <article class="card"><div class="card-icon card-icon--green"></div><h3>Listener = picker</h3><p class="card-sub">Conference participants, training guests,</p><p class="card-body">The audience starts the session by scanning the QR code or entering the dorvane code on https://dorvane.net. As soon as an interesting slide is shown, it can be picked using a button.<br>The picked slides can also be saved</p><div class="learn">LEARN MORE <svg><use href="#i-arrow"/></svg></div></article>
    <article class="card"><div class="card-icon card-icon--dark"></div><h3>Conference organizer event agency</h3><p class="card-sub">Planning and provision of the session ID</p><p class="card-body">We offer the pre-planning of a congress with many seasons about the lecture title, name of the speaker, room, time etc. We provide evaluations of the number of logged in pickers and their contact requests in various forms.</p><div class="learn">LEARN MORE <svg><use href="#i-arrow"/></svg></div></article>
  </div>
  <div class="demo">
    <div class="art" role="img" aria-label="Large mascot illustration holding the app" style="left:0;top:8px;width:170px;height:180px;border-radius:0 6px 6px 0"></div>
    <div class="phone" style="left:130px;top:95px;width:95px;height:192px"><div class="phone-screen phone-screen--demo" role="img" aria-label="Mobile app screen of an example session"></div></div>
    <div class="demo-copy" style="top:75px">
      <h2 class="demo-title">Talk to us for a demo!</h2>
      <p class="demo-text">We are currently still in the development process of the app! The basic functions are already finished and can be demonstrated.But we wanted to provide a sophisticated tool for you and your customers and we need test feedback. If you are interested, just get in touch and we will arrange a free test.</p>
      <p class="demo-note">No productive operation yet, ie no data is saved on the server.</p>
      <span class="btn btn-green">GET DEMO</span>
    </div>
  </div>
  <footer class="site-footer">
    <div class="contact"><span class="contact-icon"><svg><use href="#i-phone"/></svg></span><p>Telephone:<br>49-15120438816</p></div>
    <div class="contact"><span class="contact-icon"><svg><use href="#i-landline"/></svg></span><p>Landline:<br>+49711230574</p></div>
    <div class="contact"><span class="contact-icon"><svg><use href="#i-mail"/></svg></span><p>E-mail:<br>contact@dorvane.net</p></div>
    <div class="footer-rule"></div>
    <div class="footer-links"><span>Home</span><span class="sep">|</span><span>imprint</span><span class="sep">|</span><span>privacy</span><span class="sep">|</span><span>Contact</span><span class="sep">|</span><span>Terms &amp; Conditions</span><span class="sep">|</span><span>Privacy Statement</span></div>
    <p class="copyright">dorvane © 2020 All rights reserved.</p>
    <div class="socials"><span></span><span></span><span></span><span></span></div>
  </footer>
</section>

<!-- Variant C -->
<section class="page page--c">
  <header class="site-header">
    <div class="brand"><span>dorvane</span><span class="brand-dot"></span></div>
    <nav class="nav"><span class="is-active">Home</span><span>Subscription variants</span><span>Participant / picker</span><span>speaker</span><span>organizer</span><span>En ⌄</span></nav>
    <span class="btn btn-green nav-cta">Risk-free testing</span>
  </header>
  <div class="hero">
    <div class="hero-texture" role="img" aria-label="Soft pink abstract wave texture"></div>
    <div class="art" role="img" aria-label="Mascot illustration reaching for the app" style="left:510px;top:58px;width:175px;height:190px;border-radius:6px 0 0 6px"></div>
    <div class="phone" style="left:463px;top:152px;width:100px;height:206px"><div class="phone-screen" role="img" aria-label="Mobile app screen showing the presentation code entry"></div></div>
    <div class="hero-copy">
      <h1 class="hero-title">For the pickers:just pick your important slides</h1>
      <p class="hero-lead">Do you want qualified results of your marketing events for the further processing of the leads?</p>
    </div>
    <div class="quick quick--pickers">
      <h3>Quickstart for pickers:</h3>
      <p>Attend the lecture and pick your slides</p>
      <div class="code-label">Presentation code</div>
      <div class="code-row"><span class="code-input">presentation code</span><span class="btn btn-green">Join the presentation</span></div>
    </div>
    <div class="quick-divider"></div>
    <div class="quick quick--speaker">
      <h3>Speaker Login:</h3>
      <p>Register for your lectureshare or register.</p>
      <div class="speaker-row"><span class="btn btn-blue">Register</span><span class="or">or</span><span class="btn btn-green">To Register</span></div>
    </div>
  </div>
  <div class="speakers" role="img" aria-label="Blue backdrop with faint network pattern"></div>
  <div class="speakers" style="background:none">
    <h2 class="speakers-title">For the speakers: find your leads, get<br>feedback from the event</h2>
    <article class="card"><div class="card-icon card-icon--dark"></div><h3>Speaker, presenter with online PC</h3><p class="card-sub">The laptop must be online!</p><p class="card-body">Simply start the presentation in Slidemaker or other applications. Then call the dorvane app in the browser on app.dorvane.net. After logging in and starting the transmission, the lecture can proceed as normal.</p><div class="learn">LEARN MORE <svg><use href="#i-arrow"/></svg></div></article>
    <article class="card"><div class="card-icon card-icon--green"></div><h3>Listener = picker</h3><p class="card-sub">Conference participants, training guests,</p><p class="card-body">The audience starts the session by scanning the QR code or entering the dorvane code on https://dorvane.net. As soon as an interesting slide is shown, it can be picked using a button.<br>The picked slides can also be saved</p><div class="learn">LEARN MORE <svg><use href="#i-arrow"/></svg></div></article>
    <article class="card"><div class="card-icon card-icon--dark"></div><h3>Conference organizer event agency</h3><p class="card-sub">Planning and provision of the session ID</p><p class="card-body">We offer the pre-planning of a congress with many seasons about the lecture title, name of the speaker, room, time etc. We provide evaluations of the number of logged in pickers and their contact requests in various forms.</p><div class="learn">LEARN MORE <svg><use href="#i-arrow"/></svg></div></article>
  </div>
  <div class="demo">
    <div class="art" role="img" aria-label="Mascot illustration above the app" style="left:5px;top:5px;width:120px;height:122px"></div>
    <div class="phone" style="left:121px;top:67px;width:94px;height:192px"><div class="phone-screen phone-screen--demo" role="img" aria-label="Mobile app screen of an example session"></div></div>
    <div class="demo-copy">
      <h2 class="demo-title">Talk to us for a demo!</h2>
      <p class="demo-text">We are currently still in the development process of the app! The basic functions are already finished and can be demonstrated.But we wanted to provide a sophisticated tool for you and your customers and we need test feedback. If you are interested, just get in touch and we will arrange a free test.</p>
      <p class="demo-note">No productive operation yet, ie no data is saved on the server.</p>
      <span class="btn btn-green">GET DEMO</span>
    </div>
  </div>
  <footer class="site-footer">
    <div class="contact"><span class="contact-icon"><svg><use href="#i-phone"/></svg></span><p>Telephone:<br>49-15120438816</p></div>
    <div class="contact"><span class="contact-icon"><svg><use href="#i-landline"/></svg></span><p>Landline:<br>+49711230574</p></div>
    <div class="contact"><span class="contact-icon"><svg><use href="#i-mail"/></svg></span><p>E-mail:<br>contact@dorvane.net</p></div>
    <div class="footer-rule"></div>
    <div class="footer-links"><span>Home</span><span class="sep">|</span><span>imprint</span><span class="sep">|</span><span>privacy</span><span class="sep">|</span><span>Contact</span><span class="sep">|</span><span>Terms &amp; Conditions</span><span class="sep">|</span><span>Privacy Statement</span></div>
    <p class="copyright">dorvane © 2020 All rights reserved.</p>
    <div class="socials"><span></span><span></span><span></span><span></span></div>
  </footer>
</section>

</body>
</html>
```